Financial services referral site needs a redesign

We need a complete re-brand ; new word press design for our existing site. Need a web 2.0 clean crisp look that will convert highly. Consumers with debt come to our site so we can refer them to 3rd party providers of debt solutions ranging from credit counseling, debt consolidation, refinance and student loan consolidation. I would like to see designs that use the color green and final product should communicate safety, trust and privacy. Show case our A+ QFR rating etc. See current site at pinegroveloanaid.com

- I would like to use light blue color scheme to match the logo. The green is making it look off - I definitely need the lead form to be on the top right side of the page

```html
<!DOCTYPE html>
<html lang="en">
<head>
<meta charset="utf-8">
<title>Pine Grove Loan Aid</title>
<link rel="stylesheet" href="https://fonts.googleapis.com/css2?family=Arimo:wght@400;700&family=Open+Sans:wght@400;600;700&family=Oswald:wght@700&family=Tinos&display=swap">
<style>
:root{
  --brand:#1a8ccc;
  --nav:#1699cf;
  --nav-dark:#0b6fa5;
  --tab:#1bb3cc;
  --form:#0a72cc;
  --ink:#111;
  --grey-bg:#e9e9e9;
  --muted:#777;
  --feature-bg:#f2f2f2;
  --footer:#222;
  --seal:#e4ddd6;
}
*{box-sizing:border-box;margin:0;padding:0}
html,body{width:892px;height:1200px;overflow:hidden;background:#fff}
body{position:relative;font-family:"Arimo",Arial,sans-serif;color:var(--ink)}
.abs{position:absolute}

/* header */
.brand{left:76px;top:26px;display:flex;align-items:center;gap:10px}
.brand-dot{width:48px;height:48px;border-radius:50%;background:#7fc6dc}
.brand-name{font-family:"Tinos",serif;font-size:22px;color:var(--brand)}
.account-tab{left:669px;top:0;width:148px;height:41px;background:var(--tab);border-radius:0 0 6px 6px;text-align:center;border:1px solid #14a0b8;border-top:0}
.account-links{font-family:"Open Sans",sans-serif;font-weight:700;font-size:10px;color:#fff;margin-top:2px}
.account-phone{font-family:"Open Sans",sans-serif;font-size:15px;color:#1d3a48;margin-top:1px}
.social{display:flex;gap:8px}
.social span{width:20px;height:20px;border-radius:50%;display:block}
.social-top{left:701px;top:62px}
.social-top span{background:var(--brand)}

/* nav */
.main-nav{left:0;top:104px;width:892px;height:36px;background:var(--nav);display:flex;align-items:center;padding-left:76px}
.main-nav a{font-family:"Open Sans",sans-serif;font-weight:700;font-size:11px;color:#fff;text-decoration:none;padding:0 18px;border-right:1px solid #5dbde2;line-height:22px}
.main-nav a:last-child{border-right:0}
.main-nav a.active{background:var(--nav-dark);border:2px solid #0a5782;border-radius:4px;padding:2px 14px;margin-right:8px}

/* hero */
.hero{left:0;top:140px;width:892px;height:328px;background:var(--grey-bg)}
.slide{left:90px;top:160px;width:710px;height:274px;background:#fff;border:1px solid #d8d8d8;padding:7px 10px}
.slide-bg{width:100%;height:100%;background:linear-gradient(90deg,#fafafa 0%,#eef0ee 45%,#e4e2df 100%)}
.slide-photo{left:540px;top:168px;width:253px;height:259px;background:linear-gradient(160deg,#e8e3df 0%,#d6c5bb 45%,#f3e6ea 100%)}
.seal{left:540px;top:278px;width:100px;height:100px;border-radius:50%;background:var(--seal)}
.welcome{left:111px;top:198px;font-family:"Tinos",serif;font-size:26px}
.hero-title{left:110px;top:232px;font-family:"Oswald",sans-serif;font-weight:700;font-size:32px;color:var(--brand);letter-spacing:.3px}
.hero-quote{left:111px;top:284px;font-family:"Tinos",serif;font-size:17px;line-height:21px}
.btn-book{left:110px;top:343px;width:207px;height:32px;border-radius:16px;background:#111;color:#fff;font-family:"Open Sans",sans-serif;font-size:16px;text-align:center;line-height:32px}
.arrow{top:265px;font-size:40px;color:#888;font-family:"Open Sans",sans-serif}

/* intro */
.intro-title{left:84px;top:489px;width:420px;font-family:"Tinos",serif;font-size:22px;line-height:27px}
.intro-text{left:86px;width:416px;font-size:10.2px;line-height:15px}

/* form */
.lead-form{left:540px;top:486px;width:256px;height:268px;background:var(--form);border-radius:8px}
.form-title{left:575px;top:505px;font-family:"Open Sans",sans-serif;font-size:20px;color:#fff}
.field{position:absolute;height:24px;background:#fff;border:1px solid #c8d9ea;font-size:10px;color:#aaa;padding:5px 8px}
.field.select::after{content:"";position:absolute;right:6px;top:10px;border:4px solid transparent;border-top-color:#555}
.btn-assist{left:560px;top:709px;width:212px;height:28px;background:#111;border-radius:3px;color:#fff;font-family:"Open Sans",sans-serif;font-size:15px;text-align:center;line-height:28px}

.divider{left:86px;top:789px;width:714px;border-top:1px dashed #ccc}

/* features */
.feature{position:absolute;left:100px;width:244px;height:50px;background:var(--feature-bg);border:1px solid #ddd;border-radius:3px;font-family:"Open Sans",sans-serif;font-size:14px;color:var(--muted);padding-left:45px;display:flex;align-items:center;line-height:17px}
.feature-icon{position:absolute;left:77px;width:50px;height:50px;border-radius:50%;background:var(--form);border:2px solid #fff;box-shadow:0 0 0 1px #cfdff0}
.feature-icon svg{width:46px;height:46px}

/* news */
.news-title{left:384px;top:811px;font-family:"Tinos",serif;font-size:22px}
.news-date{left:384px;width:40px;text-align:center;font-family:"Open Sans",sans-serif;color:#555;line-height:1}
.news-date b{display:block;font-weight:400;font-size:30px}
.news-date i{display:block;font-style:normal;font-size:17px;color:#888}
.news-head{font-weight:700;font-size:9.5px;color:var(--brand);margin-bottom:2px}
.news-body{width:368px;font-size:8.9px;line-height:13.6px}
.news-more{font-size:9.5px;color:#1a4f8c}
.news-sep{left:430px;top:967px;width:385px;border-top:1px solid #e6e6e6}

/* footer */
.site-footer{left:0;top:1134px;width:892px;height:66px;background:var(--footer)}
.footer-text{left:89px;top:1151px;font-size:10px;line-height:18px;color:#fff}
.social-foot{left:690px;top:1153px}
.social-foot span{background:#999}
</style>
</head>
<body>

<header>
  <div class="abs brand"><span class="brand-dot"></span><span class="brand-name">Pine Grove Loan Aid</span></div>
  <div class="abs account-tab">
    <div class="account-links">Sign Up | Member Login</div>
    <div class="account-phone">03 9412 5580</div>
  </div>
  <div class="abs social social-top" aria-label="Social links"><span></span><span></span><span></span><span></span></div>
</header>

<nav class="abs main-nav">
  <a class="active">HOME</a><a>ABOUT US</a><a>SERVICES</a><a>HOURS &amp; LOCATION</a><a>HOME DEBT LOANS</a><a>SERVICES</a><a>CONTACT US</a>
</nav>

<section>
  <div class="abs hero"></div>
  <div class="abs arrow" style="left:56px">&#10094;</div>
  <div class="abs arrow" style="left:816px">&#10095;</div>
  <div class="abs slide"><div class="slide-bg" role="img" aria-label="Faded photo of a smiling family in the background"></div></div>
  <div class="abs slide-photo" role="img" aria-label="Photo of a smiling woman advisor"></div>
  <div class="abs seal" role="img" aria-label="Guarantee seal placeholder"></div>
  <div class="abs welcome">WELCOME TO</div>
  <div class="abs hero-title">PINE GROVE LOAN AID</div>
  <div class="abs hero-quote">"We provide the highest standards for debt solution<br>in&nbsp; most professional, and sensitive manner."</div>
  <div class="abs btn-book">Book a Appointments</div>
</section>

<section>
  <h1 class="abs intro-title" style="font-weight:400">When To Consider A Debt Consolidation Program</h1>
  <p class="abs intro-text" style="top:557px">If you're looking for a dentist in Bayview, you've come to the right place. Bright Path Dental is an established dental practice with a modern, gentle approach to oral care. Our goal is to provide quality care to every patient who walks through our doors, and we achieve this objective through attentiveness, open communication, and patient education.</p>
  <p class="abs intro-text" style="top:647px">At Bright Path Dental, we believe that a visit to the dentist should be as pleasant and stress-free as possible. That's why our dental office, located in beautiful Bayview, Seaside was designed to keep patient comfort in mind. Whether you need to schedule a general checkup or require more extensive dental work, we'll address any concerns you might have prior to treatment and answer all of your questions in a relaxed, pressure-free setting. At our dental practice, we offer:</p>

  <div class="abs lead-form"></div>
  <h2 class="abs form-title" style="font-weight:400">Our Debt Solution</h2>
  <div class="field" style="left:558px;top:545px;width:214px">First Name</div>
  <div class="field" style="left:558px;top:578px;width:215px">First Name</div>
  <div class="field" style="left:558px;top:609px;width:215px">Address</div>
  <div class="field" style="left:557px;top:643px;width:216px">Address</div>
  <div class="field select" style="left:558px;top:674px;width:98px">State</div>
  <div class="field select" style="left:666px;top:674px;width:106px">Debt Amount</div>
  <div class="abs btn-assist">Get Assistance Now !</div>
</section>

<div class="abs divider"></div>

<section>
  <div class="feature" style="top:815px">Reduce high interest<br>credit rates</div>
  <div class="abs feature-icon" style="top:815px"><svg viewBox="0 0 46 46" fill="none" stroke="#fff" stroke-width="2"><rect x="15" y="12" width="14" height="18" rx="1"/><path d="M18 18h8M18 22h8M18 26h4"/><circle cx="29" cy="30" r="5" fill="var(--form)"/><path d="M27 30l1.5 1.5 3-3"/></svg></div>
  <div class="feature" style="top:887px">Stop harassing credit calls</div>
  <div class="abs feature-icon" style="top:887px"><svg viewBox="0 0 46 46" fill="none" stroke="#fff" stroke-width="2"><rect x="13" y="13" width="9" height="9"/><rect x="24" y="13" width="9" height="9"/><rect x="13" y="24" width="9" height="9"/><rect x="24" y="24" width="9" height="9"/><path d="M15.5 17.5h4M17.5 15.5v4M15.5 28.5h4"/></svg></div>
  <div class="feature" style="top:958px">One low monthly payment</div>
  <div class="abs feature-icon" style="top:958px"><svg viewBox="0 0 46 46" fill="#fff"><path d="M23 11l12 6H11z"/><rect x="13" y="19" width="3" height="11"/><rect x="19" y="19" width="3" height="11"/><rect x="25" y="19" width="3" height="11"/><rect x="30" y="19" width="3" height="11"/><rect x="11" y="31" width="24" height="3"/></svg></div>
  <div class="feature" style="top:1029px">No costs unless you save</div>
  <div class="abs feature-icon" style="top:1029px"><svg viewBox="0 0 46 46" fill="none" stroke="#fff" stroke-width="2"><circle cx="23" cy="20" r="7"/><path d="M18 25l-4 9 4-1 2 3 3-7M28 25l4 9-4-1-2 3-3-7"/></svg></div>

  <h2 class="abs news-title" style="font-weight:400">Current Debt Relief News</h2>

  <div class="abs news-date" style="top:848px"><b>20</b><i>JAN</i></div>
  <div class="abs" style="left:433px;top:849px">
    <div class="news-head">Lorem ipsum dolor sit amet</div>
    <p class="news-body">consectetur adipisicing elit, sed do eiusmod tempor incididunt ut labore et dolore magna aliqua. Ut enim ad minim veniam, quis nostrud exercitation ullamco laboris nisi ut aliquip ex ea commodo consequat. Duis aute irure dolor in reprehenderit in voluptate velit esse cillum dolore eu fugiat nulla pariatur. Excepteur sint occaecat cupidatat non proident, sunt in culpa qui officia deserunt mollit anim id est laborum Duis aute irure dolor in reprehenderit in voluptate.</p>
  </div>
  <div class="abs news-more" style="left:757px;top:936px">More</div>
  <div class="abs news-sep"></div>

  <div class="abs news-date" style="top:990px"><b>20</b><i>JAN</i></div>
  <div class="abs" style="left:435px;top:990px">
    <div class="news-head">Lorem ipsum dolor sit amet</div>
    <p class="news-body">consectetur adipisicing elit, sed do eiusmod tempor incididunt ut labore et dolore magna aliqua. Ut enim ad minim veniam, quis nostrud exercitation ullamco laboris nisi ut aliquip ex ea commodo consequat. Duis aute irure dolor in reprehenderit in voluptate velit esse cillum dolore eu fugiat nulla pariatur. Excepteur sint occaecat cupidatat non proident, sunt in culpa qui officia deserunt mollit anim id est laborum Duis aute irure dolor in reprehenderit in voluptate.</p>
  </div>
  <div class="abs news-more" style="left:758px;top:1077px">More</div>
</section>

<footer>
  <div class="abs site-footer"></div>
  <div class="abs footer-text">Pine Grove Loan Aid - Tel: (305) 555-0148 - 210 Harbor Lane #12, Bayview, FL 33100<br>Privacy Policy | Sitemap | Terms of Use</div>
  <div class="abs social social-foot" aria-label="Social links"><span></span><span></span><span></span><span></span></div>
</footer>

</body>
</html>
```